Geschäftspapiere für landwirtschaftlichen Betrieb
Zielgruppe
Landwirtschaftlicher Betrieb, Produktion und Vermarktung von hochwertigen Bio Produkten. Spezialisiert auf Ackerbau und den Anbau von Kartoffeln. Zielgruppe sind Menschen, die bewusst qualitativ hochwertige, nachhaltig produzierte Lebensmittel schätzen.
Aufgabenstellung
Das Design soll für einen Produktanhänger gestaltet werden. Die Produktanhänger werden auf Tragetaschen aus Papier aufgenäht. Je nach Inhalt (z.B. Kartoffeln, Äpfel, Zwiebel, Süsskartoffeln,...) wird der Produktname und die Details von uns selbst mittels Thermodruck aufgedruckt. Es wird also mittig Platz benötigt. Außerdem ist wichtig, dass durch das Zunähen der Säcke auf den oberen 3cm eine Naht die Etiketten durchkreuzen wird - bitte deshalb nicht das Firmenlogo zu weit oben platzieren.
Zur Etikettengröße: Breite 6cm, Höhe 16cm. (ca. 2mm Rand, dh 5,5cm und 15,5cm können bedruckt werden)
Inhalt: Unser Logo und Anschrift (Biohof Lindner, Mühlweg 27, 3468 Auenfeld, 02281/67914, www.biohoflindner-beispiel.at, AT-Landwirtschaft AT-BIO-718). Bitte mittig auch ausreichend Platz für die Produktbezeichnung lassen.
Das Design soll eher fein und elegant sein und sich nicht auf einen bestimmten Inhalt fokussieren (z.B. nur Kartoffeln abgebildet).
Im Anhang befinden sich Fotos von den derzeitigen Etiketten.
Wir wünschen uns eine deutliche überarbeitung oder komplette Neugestalltung der Etiketten.
Im Anhang ist noch eine PDF mit den neuen Kartoffelsäcken. Vielleicht ergibt sich dabei eine neue Idee :-)

```html
<!DOCTYPE html>
<html lang="de">
<head>
<meta charset="utf-8">
<title>Produktetikett – Biohof Lindner</title>
<link rel="stylesheet" href="https://fonts.googleapis.com/css2?family=Inter:wght@400;500&display=swap">
<style>
  :root {
    --bg: #d0c6bc;
    --paper: #ffffff;
    --leaf: #c2c50c;
    --bark: #655550;
    --ink: #1c1c1c;
  }
  * { margin: 0; padding: 0; box-sizing: border-box; }
  html, body { width: 1200px; height: 785px; overflow: hidden; }
  body {
    background: var(--bg);
    font-family: "Inter", Arial, sans-serif;
    position: relative;
  }
  .label {
    position: absolute;
    left: 465px;
    top: 33px;
    width: 270px;
    height: 718px;
    background: var(--paper);
  }
  .label-shapes { position: absolute; inset: 0; width: 270px; height: 718px; }

  .brand-mark {
    position: absolute;
    left: 22px;
    width: 226px;
    top: 140px;
    display: flex;
    flex-direction: column;
    align-items: center;
    gap: 14px;
  }
  .brand-dot {
    width: 56px; height: 56px;
    border-radius: 50%;
    background: var(--leaf);
  }
  .brand-name {
    color: var(--bark);
    font-weight: 500;
    font-size: 21px;
    letter-spacing: 0.2px;
  }

  .vertical-note {
    position: absolute;
    color: var(--ink);
    font-size: 8px;
    white-space: nowrap;
    transform: rotate(-90deg);
    transform-origin: left top;
    left: 229px;
  }
  .cert-code { top: 423px; }
  .cert-authority { top: 538px; }

  .footer-name {
    position: absolute;
    left: 52px;
    top: 637px;
    width: 66px;
    color: var(--leaf);
    font-size: 9px;
    line-height: 11px;
    font-weight: 400;
  }
  .footer-contact {
    position: absolute;
    left: 136px;
    top: 635px;
    color: var(--leaf);
    font-size: 8px;
    line-height: 9.5px;
  }
  .contact-row { display: flex; gap: 6px; align-items: flex-start; margin-bottom: 3px; }
  .contact-row svg { width: 8px; height: 8px; margin-top: 1px; flex: none; fill: var(--leaf); }
  .footer-web {
    position: absolute;
    left: 22px;
    width: 226px;
    top: 683px;
    text-align: center;
    color: var(--leaf);
    font-size: 7.5px;
    letter-spacing: 0.9px;
  }
</style>
</head>
<body>
  <div class="label">
    <svg class="label-shapes" viewBox="0 0 270 718" aria-hidden="true">
      <path d="M21.7,314 Q120,284 247.5,287 L247.5,314 Q200,302 130,303 Q70,305 21.7,314 Z" fill="var(--leaf)"/>
      <path d="M21.7,589 Q140,612 247.5,589 L247.5,610 L21.7,640 Z" fill="var(--leaf)"/>
      <path d="M21.7,613 Q150,618 247.5,589 L247.5,684 Q247.5,706 225.5,706 L43.7,706 Q21.7,706 21.7,684 Z" fill="var(--bark)"/>
      <rect x="21.7" y="11.6" width="225.8" height="694.4" rx="22" fill="none" stroke="var(--leaf)" stroke-width="0.8"/>
    </svg>

    <div class="brand-mark">
      <span class="brand-dot"></span>
      <span class="brand-name">Biohof Lindner</span>
    </div>

    <span class="vertical-note cert-code">AT-BIO-718</span>
    <span class="vertical-note cert-authority">AT-Landwirtschaft</span>

    <div class="footer-name">Biohof<br>Lindner</div>
    <div class="footer-contact">
      <div class="contact-row">
        <svg viewBox="0 0 10 10"><path d="M5,0.5 L9.5,4.5 H8 V9.5 H2 V4.5 H0.5 Z"/></svg>
        <span>Mühlweg 27<br>3468 Auenfeld</span>
      </div>
      <div class="contact-row">
        <svg viewBox="0 0 10 10"><path d="M2.2,0.6 L3.8,2.8 L2.9,3.9 Q3.9,6 6.1,7.1 L7.2,6.2 L9.4,7.8 L8.5,9.3 Q4.5,9.5 1.9,6.6 Q0.3,4.4 0.7,1.5 Z"/></svg>
        <span>02281/67914</span>
      </div>
    </div>
    <div class="footer-web">www.biohoflindner-beispiel.at</div>
  </div>
</body>
</html>
```